Exterior cleaning company requires a eye catching a5 leaflet

we need some updated leaflet designs, a5 folded, we are targeting all exterior cleaning contracts, including roof cleaning & treatment, render cleaning & Treatment, driveways, block paving cleaning using the latest in low pressure cleaning technologies along side high pressure jetwashing. gutter clearance and flushing, water fed telescopic pole window cleaning of difficult to reach windows and high buildings. our website : www.tkbellowsec.co.uk facebook page: https://www.facebook.com/tkbellowsexteriorcareltd Instagram: https://www.instagram.com/tkbellowsec/ a quick google search of roof cleaning, soft washing etc will provide results of what we are doing

Target Market(s)

home owners, commercial clients

Font styles to use
Serif
Sans Serif

Requirements
Must have
• A5 Landscape folded leaflet, front page with company information and bullet points of main works : window & conservatory cleaning, roof cleaning & treatment, Render cleaning & treatment, pressure washing, soft washing, gutter clearing, pressure washing of patios, driveways, gutters, fascias (more info can be provided on techniques etc if required)

```html
<!DOCTYPE html>
<html lang="en">
<head>
<meta charset="utf-8">
<title>TK Bellows Exterior Care – A5 Leaflet</title>
<link href="https://fonts.googleapis.com/css2?family=Lato:wght@400;700;900&family=Roboto+Condensed:wght@400;700&display=swap" rel="stylesheet">
<style>
:root{
  --blue:#2a6ad8;
  --blue-deep:#2256d2;
  --blue-bright:#3b8cf2;
  --sky:#4ab0f5;
  --ink:#0a0a0a;
  --paper:#f4f4f4;
  --panel:#f2f3f5;
  --wash:#c7d7f3;
  --bg:#e4e5e7;
  --text:#1b1b1b;
  --white:#ffffff;
}
*{margin:0;padding:0;box-sizing:border-box}
html,body{width:881px;height:1200px;overflow:hidden;background:var(--bg)}
body{font-family:"Lato",sans-serif;color:var(--text)}
.artboard{position:absolute;left:0;top:0;width:1300px;height:1770px;transform:scale(.6777);transform-origin:0 0}
.sheet{position:absolute;left:120px;width:1084px;height:766px;overflow:hidden}
.sheet--outside{top:86px;background:var(--panel)}
.sheet--inside{top:903px;height:765px;background:var(--wash)}
.abs{position:absolute}
.photo{position:absolute}

/* brand */
.brand-dot{position:absolute;border:1.5px solid #333;border-radius:50%;background:transparent}
.brand-name{position:absolute;font-family:"Roboto Condensed",sans-serif;color:#111;line-height:1.1}
.brand-name b{display:block;font-weight:700}
.brand-name span{display:block;font-weight:400}
.brand-name strong{display:block;font-weight:700}

/* outside left panel */
.cover-photo{left:0;top:0;width:540px;height:204px;background:linear-gradient(90deg,#7a5544 0%,#9a7564 35%,#6f5a4c 55%,#e9ecef 75%,#cfd6dc 100%)}
.intro{left:28px;top:280px;width:494px;font-size:13.6px;line-height:15.5px;text-align:justify}
.intro p+p{margin-top:15.5px}
.contact{left:0;top:539px;width:540px;height:227px;background:var(--blue)}
.contact-pill{position:absolute;left:192px;top:-13px;width:140px;height:26px;border-radius:13px;background:var(--sky);color:var(--ink);font-size:16px;font-weight:400;text-align:center;line-height:26px}
.contact-lead{position:absolute;left:0;top:18px;width:540px;text-align:center;color:var(--white);font-size:12.5px}
.contact-icon{position:absolute;left:252px;width:28px;height:28px;border-radius:50%;background:var(--sky);display:flex;align-items:center;justify-content:center}
.contact-line{position:absolute;left:0;width:540px;text-align:center;color:var(--white);font-size:12.5px;letter-spacing:.3px}
.web-tab{position:absolute;left:144px;top:197px;width:242px;height:30px;background:var(--ink);border-radius:15px 15px 0 0;color:var(--white);font-size:13px;font-weight:700;text-align:center;line-height:28px}

/* outside right panel */
.cover-shapes{left:0;top:0;width:1084px;height:766px}
.hero-ring{left:598px;top:147px;width:384px;height:384px;border-radius:50%;border:15px solid var(--sky);background:var(--white)}
.hero-disc{left:640px;top:170px;width:338px;height:338px;border-radius:50%;overflow:hidden;background:var(--white)}
.badge{left:611px;top:597px;width:138px;height:138px;border-radius:50%;background:var(--white);border:4px solid var(--blue-bright)}
.badge-core{position:absolute;left:4px;top:4px;right:4px;bottom:4px;border-radius:50%;background:var(--ink);color:var(--white);text-align:center;padding-top:28px;line-height:1.05}
.badge-core .sm{font-size:16px;display:block}
.badge-core .lg{font-size:25px;display:block;margin:2px 0}
.services-title{left:875px;top:563px;color:var(--white);font-size:24px;font-weight:900}
.services-rule{left:875px;top:595px;width:209px;height:2px;background:var(--sky)}
.services-list{left:875px;top:603px;width:206px;list-style:none;color:var(--white);font-size:15px;line-height:17.8px;white-space:nowrap}
.services-list li::before{content:"• ";}

/* inside */
.top-stripe{left:0;top:0;width:1084px;height:15px;background:var(--blue)}
.bottom-stripe{left:0;top:752px;width:1084px;height:13px;background:var(--blue)}
.header-white{left:0;top:15px;width:542px;height:92px;background:var(--white)}
.header-pill{left:208px;top:36px;width:312px;height:46px;border-radius:23px;background:var(--blue);color:var(--white);font-size:31px;font-weight:400;text-align:center;line-height:46px}
.areas{left:542px;top:15px;width:542px;height:90px;background:var(--ink)}
.areas-title{position:absolute;left:176px;top:3px;color:var(--blue-bright);font-size:19px;font-weight:900}
.areas-col{position:absolute;top:27px;list-style:none;color:var(--white);font-size:12px;font-weight:900;line-height:14px}
.areas-col li::before{content:"• "}

.card{position:absolute;width:441px;height:138px;background:var(--paper)}
.card--right{width:447px}
.card-band{position:absolute;left:0;top:0;width:100%;height:46px}
.card-title{position:absolute;top:13px;color:var(--white);font-size:18px;font-weight:700;letter-spacing:.2px}
.card--left .card-title{left:76px}
.card--right .card-title{right:74px}
.card-text{position:absolute;top:60px;font-size:13.6px;line-height:15.5px;text-align:justify}
.card--left .card-text{left:76px;width:347px}
.card--right .card-text{left:27px;width:346px;text-align-last:right}
.thumb{position:absolute;top:15px;width:110px;height:110px;border-radius:50%;border:6px solid var(--blue);padding:4px;background:var(--white)}
.thumb--ink{border-color:var(--ink)}
.card--left .thumb{left:-52px}
.card--right .thumb{left:388px}
.thumb .photo{position:static;width:100%;height:100%;border-radius:50%}
</style>
</head>
<body>
<main class="artboard">

  <section class="sheet sheet--outside">
    <svg class="abs cover-shapes" viewBox="0 0 1084 766" aria-hidden="true">
      <defs>
        <linearGradient id="blueFade" x1="0" y1="0" x2="0" y2="1">
          <stop offset="0" stop-color="#2f86f2"/>
          <stop offset="1" stop-color="#2253d1"/>
        </linearGradient>
      </defs>
      <polygon points="545,0 635,0 735,215 690,240" fill="#8e8e8e"/>
      <polygon points="1050,0 1084,0 1084,766 635,766" fill="url(#blueFade)"/>
    </svg>

    <div class="photo cover-photo" role="img" aria-label="Photo of a brick house with a cleaner using a water fed pole and a white company van parked outside"></div>
    <span class="brand-dot" style="left:182px;top:211px;width:60px;height:60px"></span>
    <div class="brand-name" style="left:254px;top:219px">
      <b style="font-size:21px">TK Bellows</b>
      <span style="font-size:10px">Exterior Care Ltd</span>
      <strong style="font-size:11px">Tel: 01632 960 418</strong>
    </div>
    <div class="abs intro">
      <p>TK Bellows Exterior Care is Southport’s most reliable, professional cleaning company who have been providing cleaning services across the North West for 10 years! At TK Bellows, our mission is to lead our sector in providing all of our customers with an outstanding cleaning service that keeps ourselves one step ahead of our competition. All of our staff are uniformed, polite, courteous and always happy to help. We aim to build long lasting relationships with our customers, and offer a 5* customer service team to help resolve any issues that may arise.</p>
      <p>Whether it’s to improve overall results or safety, we are always on the lookout for the latest equipment that gives the best finish possible. At TK Bellows our staff use the reach &amp; wash system, otherwise known as the ‘water fed pole’. A technique which compared to traditional window cleaning, reaches your windows and frames safely from the ground, even in hard to reach areas such as above conservatories or dormer windows. This prevents any damage to your property from equipment and prevents accidents.</p>
    </div>
    <div class="abs contact">
      <div class="contact-pill">CONTACT US</div>
      <p class="contact-lead">If you wish to make further enquiries, please contact us on</p>
      <span class="contact-icon" style="top:36px">
        <svg width="16" height="16" viewBox="0 0 24 24"><path d="M6.6 10.8a15.1 15.1 0 0 0 6.6 6.6l2.2-2.2a1 1 0 0 1 1-.25 11.4 11.4 0 0 0 3.6.57 1 1 0 0 1 1 1V20a1 1 0 0 1-1 1A17 17 0 0 1 3 4a1 1 0 0 1 1-1h3.5a1 1 0 0 1 1 1c0 1.25.2 2.45.57 3.570a1 1 0 0 1-.25 1z" fill="#0d3f8c"/></svg>
      </span>
      <p class="contact-line" style="top:69px">01632 960 418</p>
      <span class="contact-icon" style="top:88px">
        <svg width="16" height="16" viewBox="0 0 24 24"><rect x="3" y="6" width="18" height="12" rx="1.5" fill="none" stroke="#0d3f8c" stroke-width="2"/><path d="M3.5 7l8.5 6.5L20.5 7" fill="none" stroke="#0d3f8c" stroke-width="2"/></svg>
      </span>
      <p class="contact-line" style="top:120px">INFO@TKBELLOWSEC.CO.UK</p>
      <span class="contact-icon" style="top:139px">
        <svg width="16" height="16" viewBox="0 0 24 24"><path d="M12 2a7 7 0 0 0-7 7c0 5 7 13 7 13s7-8 7-13a7 7 0 0 0-7-7zm0 9.5A2.5 2.5 0 1 1 12 6.5a2.5 2.5 0 0 1 0 5z" fill="#0d3f8c"/></svg>
      </span>
      <p class="contact-line" style="top:171px">14 MARLOW CLOSE, SOUTHPORT, PR9 4QT</p>
      <div class="web-tab">www.tkbellowsec.co.uk</div>
    </div>

    <span class="brand-dot" style="left:692px;top:19px;width:86px;height:86px"></span>
    <div class="brand-name" style="left:796px;top:28px">
      <b style="font-size:30px">TK Bellows</b>
      <span style="font-size:13.5px">Exterior Care Ltd</span>
      <strong style="font-size:16px;margin-top:3px">Tel: 01632 960 418</strong>
    </div>

    <div class="abs hero-ring"></div>
    <div class="abs hero-disc">
      <div class="photo" style="left:0;top:0;width:165px;height:175px;background:linear-gradient(160deg,#c9d6de,#6f7f86 60%,#8a9a6e)" role="img" aria-label="Photo of a cleaner washing a glass office frontage with a water fed pole"></div>
      <div class="photo" style="left:169px;top:0;width:169px;height:175px;background:linear-gradient(180deg,#8fa3b6,#55687a 70%,#6a7684)" role="img" aria-label="Photo of a rope access technician cleaning a high rise glass facade"></div>
      <div class="photo" style="left:0;top:179px;width:338px;height:159px;background:linear-gradient(180deg,#e6e8ea,#b9bcbf 60%,#9ea3a6)" role="img" aria-label="Photo of workers pressure washing the floor of a large empty warehouse"></div>
    </div>

    <div class="abs badge">
      <div class="badge-core">
        <span class="sm">OVER</span>
        <span class="lg">10 YEARS</span>
        <span class="sm">EXPERIENCE</span>
      </div>
    </div>

    <h2 class="abs services-title">OUR SERVICES:</h2>
    <span class="abs services-rule"></span>
    <ul class="abs services-list">
      <li>WINDOW CLEANING</li>
      <li>CONSERVATORY ROOFS</li>
      <li>ROOF CLEAN &amp; TREAT</li>
      <li>RENDER CLEAN &amp; TREAT</li>
      <li>SOFT WASHING</li>
      <li>PRESSURE WASHING</li>
      <li>DRIVEWAYS &amp; PATIOS</li>
      <li>GUTTERS &amp; FASCIAS</li>
    </ul>
  </section>

  <section class="sheet sheet--inside">
    <span class="abs top-stripe"></span>
    <div class="abs header-white"></div>
    <span class="brand-dot" style="left:30px;top:31px;width:60px;height:60px"></span>
    <div class="brand-name" style="left:102px;top:38px">
      <b style="font-size:20px">TK Bellows</b>
      <span style="font-size:10px">Exterior Care Ltd</span>
      <strong style="font-size:11px">Tel: 01632 960 418</strong>
    </div>
    <h1 class="abs header-pill">OUR SERVICES</h1>

    <div class="abs areas">
      <h3 class="areas-title">AREAS WE COVERED</h3>
      <ul class="areas-col" style="left:26px"><li>SOUTHPORT</li><li>LIVERPOOL</li><li>ORMSKIRK</li><li>AUGHTON</li></ul>
      <ul class="areas-col" style="left:216px;top:28px"><li>SCARISBRICK</li><li>TARLETON</li><li>SKELMERSDALE</li><li>BURSCOUGH</li></ul>
      <ul class="areas-col" style="left:409px;top:30px"><li>BANKS</li><li>HALSALL</li><li>FORMBY</li><li>HESKETH BANK</li></ul>
    </div>

    <article class="card card--left" style="left:82px;top:137px">
      <svg class="card-band" viewBox="0 0 441 46" preserveAspectRatio="none" aria-hidden="true"><polygon points="0,0 420,0 373,46 0,46" fill="var(--blue)"/></svg>
      <h4 class="card-title">EXTERNAL WINDOWS</h4>
      <p class="card-text">Our staff use the reach &amp; washes system otherwise known as the ‘water fed pole’. A technique which compared to traditional window cleaning, enabling us to reach your windows and frames safely from the ground.</p>
      <div class="thumb thumb--ink"><div class="photo" style="background:linear-gradient(160deg,#b7c2c9,#5d6b63 60%,#2f3a3f)" role="img" aria-label="Photo of a cleaner washing a shop front with a water fed pole"></div></div>
    </article>
    <article class="card card--left" style="left:82px;top:287px">
      <svg class="card-band" viewBox="0 0 441 46" preserveAspectRatio="none" aria-hidden="true"><polygon points="0,0 420,0 373,46 0,46" fill="var(--ink)"/></svg>
      <h4 class="card-title">INTERNAL WINDOWS</h4>
      <p class="card-text">We clean internal windows and mirrors using the dragon fly system. This method also using purified water can reach them hard to access windows again safely from the ground.</p>
      <div class="thumb"><div class="photo" style="background:linear-gradient(150deg,#dfe3e6,#aab3b9 55%,#6b7680)" role="img" aria-label="Photo of a pole brush cleaning the inside of a conservatory window"></div></div>
    </article>
    <article class="card card--left" style="left:82px;top:437px">
      <svg class="card-band" viewBox="0 0 441 46" preserveAspectRatio="none" aria-hidden="true"><polygon points="0,0 420,0 373,46 0,46" fill="var(--blue)"/></svg>
      <h4 class="card-title">CONSERVATORY ROOFS</h4>
      <p class="card-text">Has your conservatory roof started to turn green, full of bird muck or dirt? Our water pole method 99% of the time gets rid of all the dirt and grime build up that’s left on your roof.</p>
      <div class="thumb thumb--ink"><div class="photo" style="background:linear-gradient(170deg,#d6dde2,#7a5a48 50%,#4f3a30)" role="img" aria-label="Photo of a brick building with a tall glazed bay"></div></div>
    </article>
    <article class="card card--left" style="left:82px;top:587px">
      <svg class="card-band" viewBox="0 0 441 46" preserveAspectRatio="none" aria-hidden="true"><polygon points="0,0 420,0 373,46 0,46" fill="var(--ink)"/></svg>
      <h4 class="card-title">SOLAR PANELS</h4>
      <p class="card-text">Using our access equipment we can clean your solar panels. Anything that blocks the light transmission to your solar PV (or thermal) panels has the potential to lower the performance.</p>
      <div class="thumb"><div class="photo" style="background:linear-gradient(170deg,#9fb7cf,#3b4658 55%,#6e5446)" role="img" aria-label="Photo of solar panels on a tiled house roof"></div></div>
    </article>

    <article class="card card--right" style="left:560px;top:137px">
      <svg class="card-band" viewBox="0 0 447 46" preserveAspectRatio="none" aria-hidden="true"><polygon points="25,0 447,0 447,46 70,46" fill="var(--blue)"/></svg>
      <h4 class="card-title">FASCIAS &amp; GUTTERS</h4>
      <p class="card-text">Using our telescopic pressure washing lance, we can clean all of your UPVC fascia’s, gutters and drain pipes safely from the ground. The end result your fascia’s and gutters looking like brand new again.</p>
      <div class="thumb thumb--ink"><div class="photo" style="background:linear-gradient(170deg,#9ec4e6,#8e3a2e 55%,#6f7a5a)" role="img" aria-label="Photo of a red timber barn with white fascia boards"></div></div>
    </article>
    <article class="card card--right" style="left:560px;top:287px">
      <svg class="card-band" viewBox="0 0 447 46" preserveAspectRatio="none" aria-hidden="true"><polygon points="25,0 447,0 447,46 70,46" fill="var(--ink)"/></svg>
      <h4 class="card-title">DRIVEWAYS &amp; PATIOS</h4>
      <p class="card-text">From small patio areas to large driveways we clean it all. TK Bellows specialise in all driveway and patio cleaning from Indian stone, tarmac, concrete flags to block paving.</p>
      <div class="thumb"><div class="photo" style="background:linear-gradient(170deg,#8fae7a,#b98f80 35%,#9c6f62)" role="img" aria-label="Photo of a freshly cleaned block paved driveway"></div></div>
    </article>
    <article class="card card--right" style="left:560px;top:437px">
      <svg class="card-band" viewBox="0 0 447 46" preserveAspectRatio="none" aria-hidden="true"><polygon points="25,0 447,0 447,46 70,46" fill="var(--blue)"/></svg>
      <h4 class="card-title">GUTTER CLEANING</h4>
      <p class="card-text">Your property’s gutters and downpipes accumulate all sorts of debris brought by the wind. Using our high reach vac we can clean the gutters safely from the ground eliminating any falls from height.</p>
      <div class="thumb thumb--ink"><div class="photo" style="background:linear-gradient(160deg,#c3d6ea,#4d6a8c 55%,#2c3a4c)" role="img" aria-label="Photo of a gutter vacuum pole reaching a roof line"></div></div>
    </article>
    <article class="card card--right" style="left:560px;top:587px">
      <svg class="card-band" viewBox="0 0 447 46" preserveAspectRatio="none" aria-hidden="true"><polygon points="25,0 447,0 447,46 70,46" fill="var(--ink)"/></svg>
      <h4 class="card-title">PRESSURE WASHING</h4>
      <p class="card-text">We offer a wide range of pressure washing services from garden furniture to house roofs at competitive prices. Cleaning and restoration of all hard surfaces in both the domestic and commercial market.</p>
      <div class="thumb"><div class="photo" style="background:radial-gradient(circle at 60% 55%,#e7e2dd,#9b7a66 55%,#4a3328)" role="img" aria-label="Photo of a pressure washer jet spraying misty water over paving"></div></div>
    </article>

    <span class="abs bottom-stripe"></span>
  </section>

</main>
</body>
</html>
```